GUARANTEED! - Creation of Lumora Promotional Images (requires Photoshops to modify cars)

Hi all,

We will require 5 different images to be created although once the first one is completed, the look and theme can literally be copied across to the others. These promotional images are to represent the service our website offers as well as the benefit’s the user can receive. (please ask for the website via private message if required) Our website is literally a comparison website related to vehicle modifications - so we make it quick and easy for users to find the best deal with local Window Tinters, ECU Remappers, Alloy Wheel Refurbs & More.

Aim of the image - This is purely to be posted on lumora to push viewers to our website / lumora page (there will be links in the description when it’s posted on lumora) so the image needs to tell the user what we do and urge them to visit the website.

Target market - our target market is mainly the car enthusiast (ages between 17 - 25) although we’re looking to keep this promotional image simple, professional and with the use of light neutral colours.

Image to be created - (our idea, please feel free to change) - see attachment of rough sketch created titled : ‘Rough Sketch Promotional Image

Main title across the top will read ‘FIND THE BEST DEAL WITH :’ - The words best deal should stand out more and be of a larger font / potentially different colour, maybe orange to keep in theme with the website. Then as shown in the sketch, we will have car number 1 which has been photoshopped as stated further down . Then we will have arrows pointing onto the car which will state the different modifications that has been completed on the car e.g - arrow will point to the rear window and will state the words :

WINDOW TINTERS
IN YOUR AREA

(regarding the text stated above, we feel it would be best if they were all placed the same distance away from the car to keep the professional look) - we also feel the service mentioned such as ‘WINDOW TINTERS’ should be a larger font than the ‘IN YOUR AREA’

Each car will have 4 arrows pointing on different parts of the car with text added as stated above (hopefully the rough sketch will make all these requirements that little bit clearer)

Then underneath the car image with the 4 arrows and text, we will have a Call to action button (which should keep the same kind of theme as that on the website homepage, (green blackground of block with white text) - The text in this button will read ‘CLICK BELOW!’ - we also had the idea of adding an arrow under the Call to action button to point the users to the description below the image. (Needs to be clear space around the CTA so it stands out - apart from potentially this arrow)

Then finally we’d like to have our logo (quite small) to the bottom left of the image with the words ‘PLEASE SHARE!’ to the bottom right of the image.

As you can see, the requirements we’re after are quite simple so the time will be mostly in the photoshopping of the 5 cars.

Please refer to the rough sketch but if you have any questions, please contact us here.

PHOTOSHOPS REQUIRED

The changes made to each car will be partly left up to you - however it’s vitally important that it stands out yet doesn’t look ‘silly’ and needs to look realistic - looking realistic is important.

Photoshop requirements

Car 1 - Green Valtero

- Possibly change colour - please feel free to try other colours (need to look realistic)
- Change the colour of the rear window to a limo style black.
- Change the colour of the roof (can only see a slight bit of it) to black
- Change the colour of the wheels (the colour used here will depend on the change colour of the actual car, some options we like include yellow, green, orange and red

Car 2 - White Korvel ZX

- Change the colour of the rear window and rear side window to a limo style black
- Change the colour of the roof to black (not decided whether it should be black/matt black so test)
- Change the colour of the wheels to a red/ orange

Car 3 - Blue Brenn

- Possibly change colour - please feel free to try other colours - maybe a red but needs to look realistic
- Change the colour of the rear window visible to a limo style black
- Change the colour of the roof to black
- Change the colour of the wheels to black

Car 4 - Yellow Korvel ZX

- Please try changing the colour of this to a metallic grey/dark silver / gloss dark blue.
- Change the colour of the wheels to a yellow

Car 5 - Black Korvel ZX (first of all we need to remove the background of this image)

Please state if this is too difficult to photoshop and we’ll go from there.

- Colour change to red please - ensure looks realistic
- Change the colour of the wheels to a black

If any of the changes we’ve requested don’t look realistic when you’ve created them - please let us know and feel free to try other colours … remember, needs to look professional and realistic.

Background - up to you although we feel something quite neutral would work well - please however try out whatever you think would look good.

************* IMPORTANT - PLEASE READ *******************

To save you time and to avoid wasted effort, we'd like you to create the promotional image using image 1 ONLY first of all - once we're satisfied with that 100%, we would then ask you to complete the other 4 images (which shouldn't take long once the first image is complete)

*************************************************************************

Just to add - we have purchased the rights for these images but if you feel you've some car images that would suit our requirements better than these, please send them across to us for our opinion.

We may add to this brief so keep an eye out - we will also offer additional work to the winning designer - if you have any questions at all, please ask away.

Thanks,

Owen,

Still not there with the design all - keep them coming.Thanks Added Saturday, October 1, 2016

Project Deadline Extended Reason: Not happy with the designs receivec and only received a few different designers whereas the project I purchased stated I would receive alot more..Not impressed so far.Regards.Owen Added Monday, October 3, 2016

Car enthusiast / youthful - but needs to have the professional clear look - most important.

Promotional

Serif
Sans Serif

• - Title of 'FIND THE BEST DEAL WITH : '
• - Car image for each
• - 4 Arrows coming off car for each image with the text stated
• - Call to action button - that stands out
• - Logo and words 'Please share!' / 'Please share me!'
• Potential other car images (would need commercial right so would have to be free for commercial use or a suitable price to pay for the rights) - this is only if you feel you have an image that would be better than those we currently have.
• Needs to be kept clear - points to stand out are the opening title of 'FIND THE BEST DEAL WITH :', Car and the service such as 'WINDOW TINTERS'

```html
<!DOCTYPE html>
<html lang="en">
<head>
<meta charset="utf-8">
<title>Find the Best Deal – Tunewise</title>
<link rel="stylesheet" href="https://fonts.googleapis.com/css2?family=Open+Sans:ital,wght@0,600;0,800;1,700;1,800&display=swap">
<style>
  :root{
    --orange:#f26a1b;
    --ink:#1d1d1f;
    --muted:#6a6a6a;
    --line:#b9b9b9;
    --green:#1ea02b;
    --green-dark:#178622;
    --panel-top:#ffffff;
    --panel-bottom:#e6e6e6;
    --bg:#ffffff;
  }
  *{box-sizing:border-box;margin:0;padding:0}
  html,body{width:1195px;height:1200px;overflow:hidden;background:var(--bg)}
  body{position:relative;font-family:"Open Sans",Arial,sans-serif;color:var(--ink)}
  .top-band{position:absolute;left:0;top:0;width:1195px;height:8px;background:var(--orange)}
  .headline{position:absolute;left:0;top:42px;width:1195px;text-align:center;
    font-style:italic;font-weight:800;font-size:52px;letter-spacing:1px;line-height:100px}
  .headline .highlight{color:var(--orange);font-size:78px;margin:0 10px}
  .connectors{position:absolute;left:0;top:0}
  .vehicle{position:absolute;left:270px;top:340px;width:640px;height:380px;border-radius:48% 52% 30% 30%/60% 60% 28% 28%;
    background:radial-gradient(ellipse at 55% 45%,#9a9a9a 0%,#6d6d6d 55%,#2b2b2b 100%)}
  .service{position:absolute;text-align:center;padding-top:16px;
    background:linear-gradient(var(--panel-top),var(--panel-bottom));
    box-shadow:0 3px 8px rgba(0,0,0,.18);border:1px solid #dadada}
  .service-name{font-style:italic;font-weight:800;font-size:25px;line-height:30px;text-transform:uppercase}
  .service-area{font-weight:600;font-size:25px;line-height:30px;color:var(--muted)}
  .roof{left:76px;top:211px;width:282px;height:119px}
  .tint{left:760px;top:211px;width:358px;height:107px;padding-top:20px}
  .wheels{left:76px;top:750px;width:282px;height:124px}
  .ecu{left:760px;top:778px;width:358px;height:108px;padding-top:20px}
  .cta{position:absolute;left:358px;top:967px;width:468px;height:87px;background:var(--green);
    color:#fff;font-style:italic;font-weight:800;font-size:36px;letter-spacing:1px;
    display:flex;align-items:center;justify-content:center;box-shadow:inset 0 -4px 0 var(--green-dark)}
  .cta-pointer{position:absolute;left:545px;top:1066px}
  .brand{position:absolute;left:38px;top:1126px;display:flex;align-items:center;gap:12px;
    font-weight:800;font-size:30px;color:var(--ink);letter-spacing:1px}
  .brand-mark{width:20px;height:20px;background:var(--orange)}
  .share{position:absolute;right:34px;top:1116px;display:flex;align-items:center;gap:16px;
    font-style:italic;font-weight:800;font-size:34px}
</style>
</head>
<body>
  <div class="top-band"></div>
  <h1 class="headline">FIND THE <span class="highlight">BEST DEAL</span> WITH:</h1>

  <svg class="connectors" width="1195" height="1200" viewBox="0 0 1195 1200" aria-hidden="true">
    <g fill="none" stroke="var(--line)" stroke-width="2">
      <polyline points="84,330 84,432 330,432"/>
      <polyline points="760,211 566,211 566,330"/>
      <polyline points="84,750 84,553 270,553"/>
      <polyline points="1112,778 1112,538 890,538"/>
    </g>
  </svg>

  <div class="vehicle" role="img" aria-label="Grey Korvel ZX sports car with black roof, tinted rear window and yellow alloy wheels"></div>

  <svg class="connectors" width="1195" height="1200" viewBox="0 0 1195 1200" aria-hidden="true">
    <g fill="var(--green)" stroke="#fff" stroke-width="2">
      <polygon transform="translate(355,438) rotate(10)" points="-28,-7 0,-7 0,-17 28,0 0,17 0,7 -28,7"/>
      <polygon transform="translate(566,350) rotate(90)" points="-28,-7 0,-7 0,-17 28,0 0,17 0,7 -28,7"/>
      <polygon transform="translate(296,553)" points="-28,-7 0,-7 0,-17 28,0 0,17 0,7 -28,7"/>
      <polygon transform="translate(868,538) rotate(180)" points="-28,-7 0,-7 0,-17 28,0 0,17 0,7 -28,7"/>
    </g>
  </svg>

  <div class="service roof"><p class="service-name">Roof Vinyl<br>Wrappers</p><p class="service-area">in your Area</p></div>
  <div class="service tint"><p class="service-name">Window Tinters</p><p class="service-area">in your Area</p></div>
  <div class="service wheels"><p class="service-name">Alloy Wheel<br>Refurbers</p><p class="service-area">in your Area</p></div>
  <div class="service ecu"><p class="service-name">ECU Remapper</p><p class="service-area">in your Area</p></div>

  <div class="cta">SEARCH FOR FREE !</div>
  <svg class="cta-pointer" width="105" height="108" viewBox="0 0 105 108" aria-hidden="true">
    <polygon points="0,0 105,0 52,108" fill="var(--green)"/>
  </svg>

  <div class="brand"><span class="brand-mark"></span>TUNEWISE</div>

  <div class="share">
    <svg width="40" height="40" viewBox="0 0 40 40" aria-hidden="true">
      <g fill="var(--orange)" stroke="var(--orange)" stroke-width="4">
        <line x1="10" y1="20" x2="30" y2="8"/><line x1="10" y1="20" x2="30" y2="32"/>
        <circle cx="10" cy="20" r="6"/><circle cx="30" cy="8" r="6"/><circle cx="30" cy="32" r="6"/>
      </g>
    </svg>
    <span>Please Share Me</span>
  </div>
</body>
</html>
```